Local Roofing Company Billboard Design

We need a billboard design for an 8' x 32' billboard. This billboard would need to be easily readable and stand out well.
I have uploaded a design that we like - simple, readable, and gets the point across. We do NOT want the $1000 off offer included.
We are looking for a black background with white copy so it will stand out. We want the following on the billboard:
Corvella Roofing logo
corvella-roofing-example.com (optional)
555.214.7736 (mandatory)
Photo is optional, depends on how it all lays out
Production file must comply with layout requirements (uploaded).
Target Market(s)
Homeowners
Font styles to use
Other font styles liked:
- match font from logo
Colors
Designer to choose colors to be used in the design.
Requirements
Must have
- Black background, white copy, logo must be large and legible. Colors used must match our logo colors.

```html
<!DOCTYPE html>
<html lang="en">
<head>
<meta charset="utf-8">
<title>Corvella Roofing Billboard</title>
<link href="https://fonts.googleapis.com/css2?family=Montserrat:wght@500;800&family=Oswald:wght@500&display=swap" rel="stylesheet">
<style>
  :root {
    --roof-orange: #e4571e;
    --ink-black: #000000;
    --paper-white: #ffffff;
    --page-bg: #f4f4f4;
  }
  html, body {
    margin: 0;
    width: 1200px;
    height: 1051px;
    overflow: hidden;
    background: var(--page-bg);
  }
  .stage {
    width: 1200px;
    height: 1051px;
    display: flex;
    align-items: center;
    justify-content: center;
  }
  .billboard {
    width: 1120px;
    height: 280px;
    display: block;
    box-shadow: 0 18px 40px rgba(0,0,0,0.18);
  }
  .brand-name {
    font-family: "Montserrat", sans-serif;
    font-weight: 800;
    fill: var(--ink-black);
  }
  .web-address {
    font-family: "Montserrat", sans-serif;
    font-weight: 500;
    fill: var(--paper-white);
  }
  .tagline {
    font-family: "Montserrat", sans-serif;
    font-weight: 800;
    fill: var(--paper-white);
  }
  .phone-number {
    font-family: "Oswald", sans-serif;
    font-weight: 500;
    fill: var(--paper-white);
    letter-spacing: 4px;
  }
</style>
</head>
<body>
<main class="stage">
  <svg class="billboard" viewBox="0 0 1764 441" xmlns="http://www.w3.org/2000/svg" aria-label="Corvella Roofing billboard">
    <rect class="board-base" width="1764" height="441" fill="var(--paper-white)"/>

    <!-- tagline panel -->
    <polygon class="tagline-edge" points="970,0 991,0 810,253 792,253" fill="var(--roof-orange)"/>
    <polygon class="tagline-panel" points="991,0 1764,0 1764,253 810,253" fill="var(--ink-black)"/>

    <!-- phone band -->
    <polygon class="phone-band" points="808,253 1764,253 1764,441 673,441" fill="var(--roof-orange)"/>

    <!-- web band -->
    <polygon class="web-band" points="0,321 743,321 660,441 0,441" fill="var(--roof-orange)"/>

    <!-- brand name -->
    <text class="brand-name" x="45" y="205" font-size="74" textLength="690" lengthAdjust="spacingAndGlyphs">Corvella Roofing</text>

    <!-- web address -->
    <g class="laptop-icon" fill="none" stroke="var(--paper-white)" stroke-width="6">
      <rect x="62" y="360" width="40" height="28" rx="2"/>
      <path d="M54 396 H110" stroke-linecap="round"/>
    </g>
    <text class="web-address" x="128" y="393" font-size="33" textLength="505" lengthAdjust="spacingAndGlyphs">corvella-roofing-example.com</text>

    <!-- tagline -->
    <text class="tagline" x="1730" y="113" font-size="58" text-anchor="end">STRONG ROOFS FOR</text>
    <text class="tagline" x="1734" y="218" font-size="92" text-anchor="end">STRONG HOMES</text>

    <!-- phone -->
    <g class="phone-icon" fill="var(--paper-white)">
      <path d="M826 320 c6-6 14-6 18 0 l10 16 c3 6 2 11-3 15 l-6 5 c4 10 12 19 22 24 l5-6 c4-5 10-6 15-3 l16 10 c6 4 6 12 0 18 l-8 8 c-10 8-26 5-45-10 c-16-13-29-30-34-46 c-4-12-2-23 5-30 z"/>
      <path d="M862 318 a30 30 0 0 1 26 26" fill="none" stroke="var(--paper-white)" stroke-width="5" stroke-linecap="round"/>
      <path d="M864 302 a46 46 0 0 1 40 40" fill="none" stroke="var(--paper-white)" stroke-width="5" stroke-linecap="round"/>
    </g>
    <text class="phone-number" x="1730" y="400" font-size="138" text-anchor="end">555-214-7736</text>
  </svg>
</main>
</body>
</html>
```